PowerPoint Design Project for IT Consumerization presentation

I will be giving a presenatation using PP slides. The topic will the impact IT consumerization is having. I will provide the content for the slides and there will be about 20 slides. I would like for the slides to be professional designed.

It Professional

```html
<!DOCTYPE html>
<html lang="en">
<head>
<meta charset="utf-8">
<title>IT consumerization</title>
<link rel="stylesheet" href="https://fonts.googleapis.com/css2?family=Anton&display=swap">
<style>
  :root {
    --frame: #dcdde0;
    --paper: #ffffff;
    --scene-light: #f4f8fc;
    --scene-mid: #d7e4f1;
    --scene-deep: #b9cde2;
    --band-yellow: #f6e82c;
    --band-orange: #f7931e;
    --band-blue: #27a8e0;
    --band-blue-soft: #45b4e7;
    --title-top: #a9dcf6;
    --title-bottom: #2b97d6;
  }
  html, body {
    margin: 0;
    padding: 0;
    overflow: hidden;
    background: var(--paper);
  }
  .slide {
    position: relative;
    width: 1200px;
    height: 857px;
    overflow: hidden;
    background: var(--frame);
  }
  .slide-art {
    position: absolute;
    inset: 0;
    width: 1200px;
    height: 857px;
  }
  .slide-title {
    position: absolute;
    left: 474px;
    top: 700px;
    margin: 0;
    font-family: "Anton", "Impact", sans-serif;
    font-weight: 400;
    font-size: 90px;
    line-height: 1;
    letter-spacing: -1px;
    white-space: nowrap;
    background: linear-gradient(180deg, var(--title-top) 0%, #6cc3ee 45%, var(--title-bottom) 100%);
    -webkit-background-clip: text;
    background-clip: text;
    color: transparent;
    filter: drop-shadow(2px 3px 2px rgba(0, 0, 0, 0.35));
  }
</style>
</head>
<body>
<div class="slide">
  <svg class="slide-art" viewBox="0 0 1400 1000" xmlns="http://www.w3.org/2000/svg">
    <defs>
      <linearGradient id="scene-tone" x1="0" y1="0" x2="1" y2="1">
        <stop offset="0" stop-color="var(--scene-mid)"/>
        <stop offset="0.45" stop-color="var(--scene-light)"/>
        <stop offset="1" stop-color="var(--scene-deep)"/>
      </linearGradient>
    </defs>

    <rect class="paper" x="12" y="12" width="1376" height="976" fill="var(--paper)"/>

    <path class="hero-scene" role="img"
          aria-label="Glowing digital corridor with binary code floor and white silhouettes of business people walking and talking"
          fill="url(#scene-tone)"
          d="M12,12 H1388 V235 C1150,480 900,700 680,670 C500,640 300,560 12,590 Z"/>

    <path class="band band-yellow" fill="var(--band-yellow)"
          d="M12,590 C300,560 500,640 680,670 C900,700 1150,480 1388,235 V300 C1200,520 900,760 550,775 C300,790 100,840 12,895 Z"/>
    <path class="band band-orange" fill="var(--band-orange)"
          d="M12,612 C300,585 500,665 680,693 C900,722 1160,500 1388,258 V300 C1200,520 900,760 550,775 C300,790 100,840 12,895 Z"/>
    <path class="band band-blue" fill="var(--band-blue)"
          d="M12,640 C300,610 500,690 680,713 C900,740 1170,520 1388,280 V300 C1200,520 900,760 550,775 C300,790 100,840 12,895 Z"/>
    <path class="band band-blue-soft" fill="var(--band-blue-soft)"
          d="M12,735 C250,700 500,740 700,752 C950,760 1200,560 1388,300 C1200,520 900,760 550,775 C300,790 100,840 12,895 Z"/>
  </svg>

  <h1 class="slide-title">IT consumerization</h1>
</div>
</body>
</html>
```